5 Planner Covers for Teacher Planners

Hello,
I currently run a Speech-Language Pathologist website and have created a planner for my fellow Speech Therapist. I would like someone to create 5 different planner covers so my followers will have different options to choose from.
Here is my planner from last year to give you an idea of what the planner will look like http://www.talkwellnook.example/free-slp-planner/
My followers are mostly women aged 25-50. However, I don't want the covers to be overly girly or excessive with flowers. Simple is better.
I'd also like there to be an editable text box to allow the Speech Therapist to type their name on their cover if they wish.
Planner Cover can say any of the following: SLP Planner, Planner, Speech Therapy Planner, Speech-Language Pathologist (maybe this title could be editable as well??).
To give you an idea I have uploaded a screenshot of last year's planners cover that I made myself.
What I am looking for:
-Size 8.5" by 11"
-5 different planner covers
-1 gender-neutral cover
-simple design
-limited flowers (or overly girly
-text box to add a personal name
-Possible titles: SLP Planner, Planner, Speech Therapy Planner, Speech-Language Pathologist (maybe this title could be editable as well??)
Target Market(s)
Women aged 25-50
Colors
Designer to choose colors to be used in the design.
Requirements
Must have
- What I am looking for:
-Size 8.5" by 11"
-1 gender-neutral cover
-simple design
Nice to have
- I've uploaded some that I like from Craftly to give you an idea.
Here is my craftly store https://www.craftly.example/shop/QuietMeadowHome to give you an idea of things I like.
I like Marla Hensley and her simple elegant rustic style.

```html
<!DOCTYPE html>
<html lang="en">
<head>
<meta charset="utf-8">
<title>SLP Planner Cover</title>
<link rel="stylesheet" href="https://fonts.googleapis.com/css2?family=Merienda:wght@500&display=swap">
<style>
  :root {
    --backdrop: #4f4f4f;
    --paper: #ffffff;
    --blush: #fdbdbd;
    --plum: #511846;
    --meadow-green: #c9d6c4;
    --meadow-peach: #f8d3c0;
    --meadow-rose: #f1b8cc;
  }
  * { margin: 0; padding: 0; box-sizing: border-box; }
  html, body {
    width: 1200px;
    height: 1200px;
    overflow: hidden;
    background: var(--backdrop);
  }
  .planner-cover {
    position: absolute;
    left: 274px;
    top: 178px;
    width: 652px;
    height: 845px;
    background: var(--paper);
    overflow: hidden;
    font-family: "Merienda", cursive;
    color: var(--plum);
  }
  .band { position: absolute; left: 0; width: 100%; }
  .band--blush { top: 0; height: 97px; background: var(--blush); }
  .band--plum { top: 237px; height: 97px; background: var(--plum); }
  .cover-title {
    position: absolute;
    top: 130px;
    left: 0;
    width: 100%;
    text-align: center;
    font-size: 46px;
    font-weight: 500;
    font-style: italic;
    letter-spacing: 1px;
    line-height: 1;
  }
  .owner {
    position: absolute;
    top: 465px;
    left: 12px;
    width: 100%;
    text-align: center;
    font-size: 35px;
    font-weight: 500;
    font-style: italic;
    line-height: 1.2;
    letter-spacing: 1px;
  }
  .owner-name { display: block; }
  .meadow {
    position: absolute;
    left: 0;
    bottom: 0;
    width: 100%;
    height: 270px;
  }
</style>
</head>
<body>
  <main class="planner-cover">
    <div class="band band--blush"></div>
    <h1 class="cover-title">SLP Planner</h1>
    <div class="band band--plum"></div>
    <p class="owner">belongs to<span class="owner-name">xyz</span></p>
    <svg class="meadow" role="img" aria-label="Watercolour wildflower meadow along the bottom edge" viewBox="0 0 652 270" preserveAspectRatio="none">
      <defs>
        <linearGradient id="meadowFade" x1="0" y1="0" x2="0" y2="1">
          <stop offset="0" stop-color="#ffffff" stop-opacity="0"/>
          <stop offset="0.55" stop-color="var(--meadow-peach)" stop-opacity="0.45"/>
          <stop offset="1" stop-color="var(--meadow-green)" stop-opacity="0.8"/>
        </linearGradient>
      </defs>
      <rect width="652" height="270" fill="url(#meadowFade)"/>
    </svg>
  </main>
</body>
</html>
```